The Hollow - Short Film Poster Design

A short film that follows a forest ranger contemplating suicide as he stumbles upon three kids lost in the forest, each in their own, different way.

Genre: Contemporary Dark Drama

Seeking a poster that really stands out as a 'Festival Piece'. See the following lists for references:

QRVN Festival Poster Awards: https://www.snapvault.example/photos/officialqrvn/with/48203917562/

Here is the FULL RESOLUTION short film to take screen grabs and reference photos from:
https://www.filecrate.example/s/kp7wq2rzt91mxe4/Hollow014.mov?oref=e

We are open to much of anything, but this project needs to stand out as unique. On top of that, we are trying to push the angle of strangers LOST in the forest (hence the name) and have thought of the opening sequence of the young man walking through the woods on the epic wide shot of being used for the poster art.

Various items need to be included on the poster: (Please feel free to reword as appropriate)

1) A FILM BY GORDON FAIRWEATHER
2) A DENNIS HOLMGRAVE PRODUCTION

All other taglines are optional and subject to addition or removal.

Please message with all other questions and comments.
Updates

Hey everyone, I apologize for not providing a high enough resolution copy of the short. I was told that this was the highest resolution until I got back straight from my editor who said it's a preliminary. Unfortunately, I do not have the ENTIRE film at top resolution. I will, however, attach high resolution .tiffs from various points of the film for use. https://www.filecrate.example/sh/wte8pqz41nd75ub/BBXKTmcPoLRWqDYe27fhZwNtb?dl=0

Industry/Entity Type

Film Production

Font styles to use
Serif
Sans Serif

Requirements
Must have
• 1) A FILM BY GORDON FAIRWEATHER
• 2) A DENNIS HOLMGRAVE PRODUCTION
• "THE HOLLOW" - Name of Film
Nice to have
• Tagline, but not necessary.

```html
<!DOCTYPE html>
<html lang="en">
<head>
<meta charset="utf-8">
<title>The Hollow – Poster</title>
<link rel="stylesheet" href="https://fonts.googleapis.com/css2?family=Cinzel:wght@400;600;700&family=Playfair+Display:ital,wght@1,700&display=swap">
<style>
  :root {
    --paper: #ffffff;
    --silver: #d9d6d2;
    --blood: #c61f2a;
    --ghost: rgba(230, 220, 210, 0.14);
    --hill-top: #8d7563;
    --hill-mid: #6b5443;
    --brush: #4a3a2c;
    --ground: #3b2e24;
  }
  html, body {
    margin: 0;
    padding: 0;
    width: 810px;
    height: 1200px;
    overflow: hidden;
    background: var(--ground);
  }
  .poster {
    position: relative;
    width: 810px;
    height: 1200px;
    overflow: hidden;
  }
  .scene {
    position: absolute;
    inset: 0;
    background:
      radial-gradient(ellipse at 78% 68%, rgba(40, 28, 22, 0.55), transparent 38%),
      linear-gradient(180deg, var(--hill-top) 0%, var(--hill-mid) 30%, var(--brush) 62%, var(--ground) 100%);
  }
  .giant {
    position: absolute;
    margin: 0;
    font-family: "Playfair Display", Georgia, serif;
    font-style: italic;
    font-weight: 700;
    color: var(--paper);
    line-height: 1;
    white-space: nowrap;
  }
  .giant--top { font-size: 560px; left: 340px; top: -170px; }
  .giant--left { font-size: 560px; left: -150px; top: 560px; }
  .giant--bottom { font-size: 560px; left: 30px; top: 905px; }
  .ghost {
    position: absolute;
    margin: 0;
    font-family: "Cinzel", serif;
    color: var(--ghost);
    white-space: nowrap;
    line-height: 1;
  }
  .ghost--mid { font-size: 70px; left: 395px; top: 418px; }
  .ghost--low { font-size: 70px; left: 110px; top: 960px; }
  .ghost--base { font-size: 150px; left: -10px; top: 1050px; }
  .title-block {
    position: absolute;
    left: 80px;
    top: 500px;
    font-family: "Cinzel", serif;
  }
  .genre {
    margin: 0 0 4px 28px;
    font-size: 14px;
    letter-spacing: 0.5px;
    color: var(--paper);
    font-variant: small-caps;
  }
  .title { margin: 0; line-height: 0.86; }
  .title__the {
    display: block;
    margin-left: 22px;
    font-size: 112px;
    font-weight: 700;
    color: var(--silver);
  }
  .title__name {
    display: block;
    font-size: 112px;
    font-weight: 700;
    color: var(--blood);
    letter-spacing: -2px;
  }
  .credits {
    position: absolute;
    left: 74px;
    top: 812px;
    font-family: "Cinzel", serif;
    color: var(--paper);
  }
  .credits p { margin: 0; line-height: 1.2; }
  .credits__label { font-size: 28px; }
  .credits__director { font-size: 30px; font-weight: 600; margin-bottom: 22px !important; }
  .credits__producer { font-size: 27px; letter-spacing: 0.5px; }
</style>
</head>
<body>
  <main class="poster">
    <div class="scene" role="img" aria-label="Wide shot of a dry forest canyon with bare trees; a young man with a red backpack walks through the brush on the right"></div>

    <p class="ghost ghost--mid" aria-hidden="true">THE HOLLOW</p>
    <p class="ghost ghost--low" aria-hidden="true">THE HOLLOW</p>
    <p class="ghost ghost--base" aria-hidden="true">THE HOLLOW</p>

    <p class="giant giant--top" aria-hidden="true">ol</p>
    <p class="giant giant--left" aria-hidden="true">l</p>
    <p class="giant giant--bottom" aria-hidden="true">ho</p>

    <header class="title-block">
      <p class="genre">Contemporary Dark Drama</p>
      <h1 class="title">
        <span class="title__the">THE</span>
        <span class="title__name">HOLLOW</span>
      </h1>
    </header>

    <section class="credits">
      <p class="credits__label">A FILM BY</p>
      <p class="credits__director">GORDON FAIRWEATHER</p>
      <p class="credits__producer">A DENNIS HOLMGRAVE</p>
      <p class="credits__producer">PRODUCTION</p>
    </section>
  </main>
</body>
</html>
```